Creative Brief
business card ZOVRELLA HAIR CARE
ZOVRELLA HAIR CARE
Bright & Fun-filled
DORIAN FELKOSTA
PO Box 5817 WILLOWMERE
CA 90478
df@zovrellahair-example.com
zovrellahair-example.com
current logo
tire tracks

```html
<!DOCTYPE html>
<html lang="en">
<head>
<meta charset="utf-8">
<title>Zovrella Hair Care Stationery</title>
<link rel="stylesheet" href="https://fonts.googleapis.com/css2?family=Montserrat:wght@400;600;800&display=swap">
<style>
:root{
  --bg:#e7e5e0;
  --paper:#ffffff;
  --lime:#8dc63f;
  --lime-dark:#5e8f1f;
  --ink:#1c1c1c;
  --grey-dark:#5d5d5d;
  --line:#c9c9c9;
  --faint:#eef5e3;
}
*{box-sizing:border-box;margin:0;padding:0}
html,body{width:1200px;height:641px;overflow:hidden}
body{background:var(--bg);font-family:'Montserrat',sans-serif;color:var(--ink);position:relative}
.piece{position:absolute;background:var(--paper);box-shadow:0 2px 6px rgba(0,0,0,.18);overflow:hidden}
.brand{font-family:'Montserrat',sans-serif;font-weight:800;color:var(--lime);letter-spacing:.3px;white-space:nowrap}
.splatter{position:absolute;background:linear-gradient(90deg,rgba(141,198,63,0),var(--lime) 22%,#3a3a2a 55%,var(--ink) 80%,var(--lime) 100%)}

/* business cards */
.card{width:156px;height:60px;top:29px}
.card .brand{position:absolute;font-size:7px}
.card-front{left:228px}
.card-front .brand{left:60px;top:6px}
.card-front .photo{position:absolute;left:4px;top:14px;width:52px;height:40px;background:linear-gradient(135deg,#6d6d6d,#2b2b2b)}
.card-front .details{position:absolute;left:61px;top:18px;font-size:4px;line-height:6px;color:var(--ink);white-space:nowrap}
.card-front .details strong{font-size:4.8px}
.card-products{left:396px}
.card-products .brand{left:6px;top:6px}
.card-products .photo{position:absolute;left:8px;top:18px;width:140px;height:38px;background:linear-gradient(90deg,#2a2a2a,#b33a2a 30%,#8dc63f 60%,#1f1f1f)}
.card-green{left:560px;background:linear-gradient(160deg,var(--lime),var(--lime-dark))}
.card-green .brand{left:6px;top:6px;color:var(--paper)}
.card-green .photo{position:absolute;left:40px;top:20px;width:110px;height:36px;background:linear-gradient(90deg,#2b2b2b,#7a2a20 50%,#2b2b2b)}

/* letters */
.letter{top:125px;width:322px;height:456px}
.fax{left:43px}
.letterhead{left:384px}
.letter .header{position:absolute;left:0;top:0;width:100%;height:58px}
.letter .header .splatter{left:150px;top:4px;width:172px;height:52px}
.letter .header .brand{position:absolute;left:12px;top:20px;font-size:13px}
.watermark{position:absolute;left:14px;top:318px;font-size:26px;font-weight:800;color:var(--faint);white-space:nowrap}
.footer{position:absolute;left:0;bottom:10px;width:100%;text-align:center;font-size:4.5px;line-height:7px;color:var(--grey-dark)}

.fax-title{position:absolute;right:16px;top:86px;font-size:13px;font-weight:800;letter-spacing:.5px}
.fax-fields{position:absolute;left:12px;top:104px;width:298px;display:grid;grid-template-columns:1fr 1fr;column-gap:14px;row-gap:6px}
.field{display:flex;align-items:flex-end;font-size:5px;color:var(--grey-dark);border-bottom:1px solid var(--line);height:10px;padding-bottom:1px}
.fax-options{position:absolute;left:12px;top:172px;display:flex;gap:16px;font-size:5px;color:var(--grey-dark)}
.fax-options span::before{content:"";display:inline-block;width:5px;height:5px;border:.6px solid var(--grey-dark);border-radius:50%;margin-right:3px;vertical-align:-1px}

/* envelopes */
.envelope{left:734px;width:418px;height:110px}
.envelope-white{top:18px}
.envelope-green{top:145px}
.envelope-grey{top:272px}
.flap{position:absolute;left:0;top:0;width:100%;height:44px;display:flex;align-items:center;justify-content:center}
.flap svg{position:absolute;left:0;top:0}
.flap .brand{position:relative;font-size:16px;color:var(--paper);margin-top:-6px}
.envelope-white .brand-top{position:absolute;left:0;width:100%;text-align:center;top:12px;font-size:16px}

/* compliments slip */
.slip{left:734px;top:413px;width:418px;height:168px}
.slip .header{position:absolute;left:0;top:0;width:100%;height:56px}
.slip .header .splatter{left:200px;top:4px;width:218px;height:48px}
.slip .header .brand{position:absolute;left:12px;top:19px;font-size:14px}
.slip .rule{position:absolute;left:10px;right:10px;top:62px;border-top:1px solid var(--line)}
.slip .footer{bottom:8px}
</style>
</head>
<body>

<section class="piece card card-front" aria-label="Business card front">
  <div class="photo" role="img" aria-label="Photograph of a classic car"></div>
  <div class="brand">ZOVRELLA HAIR CARE</div>
  <div class="details"><strong>DORIAN FELKOSTA</strong><br>PO Box 5817 WILLOWMERE<br>CA 90478<br>df@zovrellahair-example.com<br>zovrellahair-example.com</div>
</section>
<section class="piece card card-products" aria-label="Business card back">
  <div class="brand">ZOVRELLA HAIR CARE</div>
  <div class="photo" role="img" aria-label="Photograph of hair care product bottles"></div>
</section>
<section class="piece card card-green" aria-label="Business card alternate back">
  <div class="brand">ZOVRELLA HAIR CARE</div>
  <div class="photo" role="img" aria-label="Photograph of hair care products on green"></div>
</section>

<section class="piece letter fax" aria-label="Fax cover sheet">
  <div class="header">
    <div class="splatter" role="img" aria-label="Grunge tire-track splatter in lime green and black"></div>
    <div class="brand">ZOVRELLA HAIR CARE</div>
  </div>
  <div class="fax-title">FAX</div>
  <div class="fax-fields">
    <div class="field">To:</div><div class="field">From:</div>
    <div class="field">Fax:</div><div class="field">Pages:</div>
    <div class="field">Phone:</div><div class="field">Date:</div>
    <div class="field">Re:</div><div class="field">CC:</div>
  </div>
  <div class="fax-options"><span>Urgent</span><span>For Review</span><span>Please Comment</span><span>Please Reply</span><span>Please Recycle</span></div>
  <div class="watermark" aria-hidden="true">ZOVRELLA HAIR CARE</div>
  <div class="footer">PO Box 5817 WILLOWMERE CA 90478<br>df@zovrellahair-example.com · zovrellahair-example.com</div>
</section>

<section class="piece letter letterhead" aria-label="Letterhead">
  <div class="header">
    <div class="splatter" role="img" aria-label="Grunge tire-track splatter in lime green and black"></div>
    <div class="brand">ZOVRELLA HAIR CARE</div>
  </div>
  <div class="watermark" aria-hidden="true">ZOVRELLA HAIR CARE</div>
  <div class="footer">PO Box 5817 WILLOWMERE CA 90478<br>df@zovrellahair-example.com · zovrellahair-example.com</div>
</section>

<section class="piece envelope envelope-white" aria-label="Envelope white">
  <div class="brand brand-top">ZOVRELLA HAIR CARE</div>
</section>
<section class="piece envelope envelope-green" aria-label="Envelope green flap">
  <div class="flap">
    <svg width="418" height="44" viewBox="0 0 418 44" aria-hidden="true">
      <defs><linearGradient id="flapGreen" x1="0" x2="1"><stop offset="0" stop-color="#6fa52b"/><stop offset=".5" stop-color="#9bd14d"/><stop offset="1" stop-color="#6fa52b"/></linearGradient></defs>
      <path d="M0 0H418V30Q209 48 0 30Z" fill="url(#flapGreen)"/>
    </svg>
    <div class="brand">ZOVRELLA HAIR CARE</div>
  </div>
</section>
<section class="piece envelope envelope-grey" aria-label="Envelope grey flap">
  <div class="flap">
    <svg width="418" height="44" viewBox="0 0 418 44" aria-hidden="true">
      <defs><linearGradient id="flapGrey" x1="0" x2="1"><stop offset="0" stop-color="#6a6a6a"/><stop offset=".5" stop-color="#a3a3a3"/><stop offset="1" stop-color="#6a6a6a"/></linearGradient></defs>
      <path d="M0 0H418V30Q209 48 0 30Z" fill="url(#flapGrey)"/>
    </svg>
    <div class="brand">ZOVRELLA HAIR CARE</div>
  </div>
</section>

<section class="piece slip" aria-label="Compliments slip">
  <div class="header">
    <div class="splatter" role="img" aria-label="Grunge tire-track splatter in lime green and black"></div>
    <div class="brand">ZOVRELLA HAIR CARE</div>
  </div>
  <div class="rule"></div>
  <div class="footer">PO Box 5817 WILLOWMERE CA 90478 · df@zovrellahair-example.com · zovrellahair-example.com</div>
</section>

</body>
</html>
```